Coffee to go business card

Can you make an Orange card please.
our other colours are black chocolate and white for the writing.
If you could make the name and phone number more prominant.

Target Market(s)

People on the go.

Industry/Entity Type

Business

Contact Information for Business Card

Tarvo Espresso Bar - coffee to go
Open at the Orange window
Weekdays 5.30am to 2.30pm
Saturdays 7.30am to 2.00pm
Phone orders welcome 47918306
Shop 9 Linden Vale Centre
17 Barrow Street, Linden VAle, 4812
Serving Fresh Vasko Espresso
Like us on Chatterbox

Requirements
Must have
• I have attached our logo but not dure if it uploaded correctly?
Nice to have
• see above

```html
<!DOCTYPE html>
<html lang="en">
<head>
<meta charset="utf-8">
<title>Tarvo Espresso Bar – business card, sides A and B</title>
<link rel="stylesheet" href="https://fonts.googleapis.com/css2?family=PT+Sans:wght@400;700&family=Kaushan+Script&display=swap">
<style>
  :root {
    --page: #e4e4e4;
    --orange: #fb7d05;
    --orange-light: #fd9a2c;
    --chocolate: #3a0c08;
    --white: #ffffff;
    --label: #f4f4f4;
    --sans: "PT Sans", Arial, sans-serif;
    --script: "Kaushan Script", cursive;
  }
  * { box-sizing: border-box; margin: 0; padding: 0; }
  html, body {
    width: 979px; height: 1200px; overflow: hidden;
    background: var(--page);
    font-family: var(--sans);
  }
  .canvas { position: relative; width: 979px; height: 1200px; }

  .card {
    position: absolute; left: 132px; width: 712px; height: 438px;
    background: var(--orange);
    border-radius: 17px;
    overflow: hidden;
    box-shadow: 0 8px 14px rgba(0,0,0,0.22);
  }
  .card--front { top: 67px; }
  .card--back { top: 645px; }

  .swoosh { position: absolute; inset: 0; width: 100%; height: 100%; }
  .swoosh path { fill: none; stroke: var(--orange-light); stroke-width: 34; stroke-linecap: round; }

  .side-label {
    position: absolute; left: 0; width: 979px; text-align: center;
    font-family: Arial, Helvetica, sans-serif; font-weight: 700;
    font-size: 40px; color: var(--label);
  }
  .side-label--a { top: 534px; }
  .side-label--b { top: 1108px; }

  .brand-name {
    position: absolute; color: var(--white);
    font-weight: 700; letter-spacing: 0.5px; line-height: 1.05;
  }
  .card--front .brand-name {
    top: 92px; left: 0; width: 100%; text-align: center; font-size: 60px;
  }
  .card--back .brand-name {
    top: 105px; left: 46px; font-size: 54px;
  }

  .address {
    position: absolute; top: 250px; left: 0; width: 100%;
    text-align: center; color: var(--white);
    font-weight: 700; font-size: 28px; line-height: 37px;
  }
  .phone-caption {
    position: absolute; top: 333px; left: 0; width: 100%;
    text-align: center; color: var(--chocolate);
    font-weight: 700; font-size: 25px;
  }
  .phone-number {
    position: absolute; top: 364px; left: 0; width: 100%;
    text-align: center; color: var(--white);
    font-weight: 700; font-size: 46px; letter-spacing: 1px;
    -webkit-text-stroke: 1.5px #6b6b6b;
    text-shadow: 0 3px 3px rgba(0,0,0,0.35);
  }

  .hours {
    position: absolute; top: 72px; left: 420px; width: 260px;
    text-align: center; color: var(--white); font-weight: 700;
  }
  .hours__title { font-size: 31px; margin-bottom: 18px; }
  .hours__days { font-size: 18px; margin-bottom: 8px; }
  .hours__time { font-size: 27px; margin-bottom: 14px; }

  .tagline {
    position: absolute; top: 318px; left: 420px; width: 260px;
    text-align: center; color: var(--chocolate);
    font-family: var(--script); font-size: 29px; line-height: 52px;
    transform: rotate(-6deg);
  }

  .social {
    position: absolute; top: 377px; left: 61px;
    color: var(--white); font-weight: 700; font-size: 19px;
  }
  .social__name { font-size: 26px; margin-left: 4px; }
</style>
</head>
<body>
<main class="canvas">

  <section class="card card--front" aria-label="Business card front">
    <svg class="swoosh" viewBox="0 0 712 438" aria-hidden="true">
      <path d="M600 -10 C650 120 430 170 320 250 S190 380 175 450"/>
    </svg>
    <h1 class="brand-name">Tarvo Espresso Bar</h1>
    <p class="address">Shop 9 Linden Vale Centre, 17 Barrow Street<br>Linden Vale, Queensland 4812</p>
    <p class="phone-caption">Phone orders welkome:</p>
    <p class="phone-number">47918306</p>
  </section>
  <p class="side-label side-label--a">side A</p>

  <section class="card card--back" aria-label="Business card back">
    <svg class="swoosh" viewBox="0 0 712 438" aria-hidden="true">
      <path d="M600 -10 C640 110 400 190 280 260 S110 390 95 450"/>
    </svg>
    <h2 class="brand-name">Tarvo<br>Espresso Bar</h2>
    <div class="hours">
      <p class="hours__title">Opening hours:</p>
      <p class="hours__days">Monday to Friday</p>
      <p class="hours__time">5:30 am to 2:30 pm</p>
      <p class="hours__days">Saturday</p>
      <p class="hours__time">7:30 am to 2:00 pm</p>
    </div>
    <p class="tagline">Serving Fresh<br>Vasko Espresso!</p>
    <p class="social">Like us on: <span class="social__name">Chatterbox</span></p>
  </section>
  <p class="side-label side-label--b">side B</p>

</main>
</body>
</html>
```